Report redesign

We need a designer to redesign the attached report and provide us with a template so we can use it for future reports. We want the redesigned report to look like the one in this link:

http://www3.lumatrexa.org/docs/LTX_SCT_RRN_NewModelsAddressingSupplyChainTransportRisk_IndustryAgenda_2012.pdf

Colors
0392cd
3176b5
85acd3
85cae6
33a6d7
0292cd
33b8a4

```html
<!DOCTYPE html>
<html lang="en">
<head>
<meta charset="utf-8">
<title>Verdantis – Legal Disclaimer and Study Authors</title>
<link rel="stylesheet" href="https://fonts.googleapis.com/css2?family=Arimo:wght@400;700&display=swap">
<style>
  :root {
    --brand-blue: #0392cd;
    --brand-deep: #3176b5;
    --brand-sky: #85cae6;
    --ink: #1a1a1a;
    --muted: #8a8a8a;
    --paper: #ffffff;
    --footer-dark: #000000;
    --footer-grey: #808080;
  }
  * { box-sizing: border-box; margin: 0; padding: 0; }
  html, body { width: 849px; height: 1200px; overflow: hidden; background: var(--paper); }
  body { font-family: "Arimo", Helvetica, Arial, sans-serif; color: var(--ink); }
  .page { position: relative; width: 849px; height: 1200px; overflow: hidden; }

  .brand { position: absolute; top: 38px; right: 38px; text-align: right; }
  .brand-row { display: flex; align-items: center; justify-content: flex-end; gap: 8px; }
  .brand-dot { width: 28px; height: 28px; border-radius: 50%; background: var(--brand-blue); }
  .brand-name { font-size: 27px; font-weight: 700; color: #3a3a3a; letter-spacing: 0.5px; line-height: 1; }
  .brand-tagline { font-size: 15px; color: var(--muted); margin-top: 3px; }

  .disclaimer { position: absolute; left: 109px; top: 209px; width: 670px; }
  .disclaimer h2 { font-size: 16px; font-weight: 700; color: var(--brand-deep); margin-bottom: 8px; }
  .disclaimer p { font-size: 15px; line-height: 19px; text-align: justify; }

  .authors-panel { position: absolute; left: 0; top: 465px; width: 211px; height: 352px; background: var(--brand-blue); }
  .authors-panel svg { position: absolute; left: 82px; top: 118px; }

  .authors { position: absolute; left: 245px; top: 469px; }
  .authors h3 { font-size: 17px; font-weight: 700; color: var(--brand-deep); margin-bottom: 22px; }
  .author { font-size: 15px; line-height: 21.5px; margin-bottom: 21px; }
  .author-name { color: var(--brand-deep); font-weight: 700; }

  .footer { position: absolute; left: 0; top: 1120px; width: 849px; height: 80px; display: flex; gap: 2px; }
  .footer-note { width: 568px; background: var(--footer-dark); color: #fff; font-size: 12px; line-height: 16px; padding: 23px 0 0 0; }
  .footer-note span { display: block; width: 386px; text-align: center; }
  .footer-page { flex: 1; background: var(--footer-grey); color: #fff; font-size: 15px; text-align: right; padding: 24px 32px 0 0; }
</style>
</head>
<body>
<div class="page">
  <header class="brand">
    <div class="brand-row">
      <span class="brand-dot"></span>
      <span class="brand-name">VERDANTIS</span>
    </div>
    <div class="brand-tagline">powering what's next</div>
  </header>

  <section class="disclaimer">
    <h2>LEGAL DISCLAIMER</h2>
    <p>Verdantis makes no representation or warranty as to the accuracy or completeness of the material herein and shall have and accept no liability for any statements, opinions, information or matters (expressed or implied) arising out of, contained in or derived from this document or any omissions from this document, or any other written or oral communication transmitted or made available to any other party in relation to the subject matter of this document. Any use which a third party makes of the work, or any reliance on or decisions to be made based on it, are the responsibility of such third parties. Decisions made or actions taken as a result of our work shall be the responsibility of the parties directly involved in the decisions or actions.</p>
  </section>

  <aside class="authors-panel">
    <svg width="94" height="94" viewBox="0 0 94 94" aria-hidden="true">
      <circle cx="47" cy="47" r="44" fill="none" stroke="#ffffff" stroke-width="4"/>
    </svg>
  </aside>

  <section class="authors">
    <h3>Study authors:</h3>
    <div class="author"><span class="author-name">Dana Whitcombe</span> – Managing Director<br>dana.whitcombe@verdantis.net</div>
    <div class="author"><span class="author-name">Grant Ellery</span> – Head of Business Development<br>grant.ellery@verdantis.net</div>
    <div class="author"><span class="author-name">Tomasz Kowalczyk</span> – Manager of Operations and Product Development<br>tomasz@verdantis.net</div>
    <div class="author"><span class="author-name">Luc-André Beaumier</span> – Biomass Consultant and Project Manager<br>la@verdantis.net</div>
    <div class="author"><span class="author-name">Owen Castellan</span> – Biomass Consultant and Supply Analyst<br>owen@verdantis.net</div>
  </section>

  <footer class="footer">
    <div class="footer-note">
      <span>Prepared for Meadowline Specialty Spirits Inc.</span>
      <span>Confidential © 2015 Verdantis Inc.</span>
    </div>
    <div class="footer-page">2</div>
  </footer>
</div>
</body>
</html>
```